Website redesign www.tidecrestpc.com law firm site

Need to redesign the website that I currently have to look more modern and professional. Would also like to be able to make updates and post without having a huge hassle. See current www.tidecrestpc.com. I just think that it looks very immature and it's very templated there's no ability for me to make posts or Add links or anything like that

Target Market(s)

California people looking for a powerhouse attorney in

Industry/Entity Type

Legal

Number of Pages Required

3 page

Font styles to use
Serif
Sans Serif

Colors
ec1f27
000000
ffffff

Requirements
Must have
• Must be mobile friendly. Must look professional and have ability to post links to other websites. Must have ability to post blogs or articles. Would like to be able to read my TallyDock account and also have the ability to upload forms for people to download
Nice to have
• Simple design easy to use and not cluttered with too much text

```html
<!DOCTYPE html>
<html lang="en">
<head>
<meta charset="utf-8">
<title>Tidecrest Law, P.C. — Chico California Attorney</title>
<link rel="stylesheet" href="https://fonts.googleapis.com/css2?family=Gelasio:wght@400;500&family=Open+Sans:wght@400;600&family=Raleway:wght@500;600&display=swap">
<style>
:root{
  --red:#ec1f27;
  --black:#000000;
  --ink:#2b2b2b;
  --muted:#8a8a8a;
  --white:#ffffff;
  --grey-band:#ececec;
  --footer-bar:#262626;
  --serif:"Gelasio", Georgia, serif;
  --sans:"Open Sans", Arial, sans-serif;
  --nav:"Raleway", Arial, sans-serif;
}
*{margin:0;padding:0;box-sizing:border-box}
html,body{width:1200px;height:2341px;overflow:hidden}
body{position:relative;background:var(--white);font-family:var(--sans);color:var(--ink)}
.abs{position:absolute}

/* hero */
.hero{left:0;top:0;width:1200px;height:557px;background:linear-gradient(135deg,#3a2a1e 0%,#5b4330 40%,#2a1d14 75%,#1a120c 100%)}
.nav-rule{height:1px;background:rgba(255,255,255,.25)}
.nav a{position:absolute;top:63px;font-family:var(--nav);font-weight:600;font-size:15px;color:var(--white);text-decoration:none;letter-spacing:.2px}
.nav a.active{color:var(--red)}
.brand{left:476px;top:52px;width:248px;text-align:center;color:var(--white);font-family:var(--serif);font-weight:400;font-size:30px;line-height:36px;white-space:nowrap}
.hero-title{left:141px;font-family:var(--serif);font-weight:400;color:var(--white);white-space:nowrap}
.hero-title.l1{top:237px;font-size:31px}
.hero-title.l2{top:283px;font-size:43px}
.btn-red{left:142px;top:346px;width:134px;height:41px;background:var(--red);border-radius:4px;color:var(--white);font-family:var(--nav);font-weight:600;font-size:14px;display:flex;align-items:center;justify-content:center}
.dots{left:553px;top:516px;display:flex;gap:6px}
.dots span{width:19px;height:19px;border-radius:50%;background:rgba(255,255,255,.45)}
.dots span:first-child{background:var(--white)}

/* welcome */
.welcome h2{left:137px;top:614px;font-family:var(--serif);font-weight:400;font-size:28px;color:var(--ink)}
.welcome p{left:137px;width:490px;font-size:12.5px;line-height:20px;color:var(--muted)}
.btn-dark{left:137px;top:827px;width:113px;height:34px;background:#2b2b2b;border-radius:4px;color:var(--white);font-family:var(--nav);font-weight:600;font-size:12px;display:flex;align-items:center;justify-content:center}
.cloud{left:663px;top:605px;width:398px;height:256px;background:radial-gradient(ellipse at center,#6b1a1a 0%,#a5602c 45%,#ffffff 75%)}

/* practice */
.practice{left:0;top:916px;width:1200px;height:350px;background:linear-gradient(90deg,rgba(236,31,39,.9),rgba(226,24,32,.85) 50%,rgba(236,31,39,.9)),linear-gradient(90deg,#7a1a1a,#b43a3a,#7a1a1a)}
.practice-title{left:0;width:1200px;top:945px;text-align:center;font-family:var(--serif);font-weight:400;font-size:28px;color:var(--white)}
.area{top:1006px;width:234px;text-align:center;color:var(--white)}
.area svg{display:block;margin:0 auto}
.area h3{margin-top:12px;font-family:var(--serif);font-weight:400;font-size:20px;text-transform:uppercase}
.area p{margin-top:6px;font-size:12px;line-height:17px;color:rgba(255,255,255,.85)}

/* intro cards */
.band-grey{left:0;top:1266px;width:1200px;height:373px;background:var(--grey-band)}
.card{background:var(--white);border:1px solid #dddddd}
.card h3{position:absolute;left:22px;top:20px;font-family:var(--serif);font-weight:400;font-size:21px;color:var(--black)}
.card .ph{position:absolute;left:21px;top:58px;width:196px;height:147px}
.card p{position:absolute;left:235px;top:58px;width:200px;font-size:12px;line-height:20.5px;color:var(--muted)}

/* blogs */
.blogs h2{left:141px;top:1669px;font-family:var(--serif);font-weight:400;font-size:28px;color:var(--red)}
.post{top:1721px;width:292px;height:264px;background:var(--white);border:1px solid #dddddd}
.post .ph{height:150px}
.post h3{margin:14px 0 0 18px;font-family:var(--sans);font-weight:400;font-size:15px;color:var(--red);white-space:nowrap}
.post p{margin:5px 14px 0 18px;font-size:11px;line-height:18px;color:var(--muted)}
.post .more{display:block;margin:4px 0 0 18px;font-family:var(--nav);font-weight:600;font-size:12px;color:var(--black)}

/* footer */
.footer{left:0;top:2047px;width:1200px;height:200px;background:linear-gradient(90deg,#141414 0%,#1c2233 50%,#13213d 100%)}
.foot-brand{left:150px;top:2106px;width:215px;text-align:center;color:var(--white);font-family:var(--serif);font-weight:400;font-size:27px;line-height:34px;white-space:nowrap}
.fcol{top:2102px;color:var(--white)}
.fcol h4{font-family:var(--nav);font-weight:500;font-size:16px;margin-bottom:11px;text-transform:uppercase}
.fcol li{list-style:none;font-size:12px;line-height:23px;display:flex;align-items:center;gap:6px;white-space:nowrap}
.social{display:flex;gap:14px}
.social span{width:29px;height:29px;border-radius:50%;background:var(--black)}
.bar{left:0;top:2247px;width:1200px;height:94px;background:var(--footer-bar)}
.bar p{position:absolute;left:0;width:1200px;top:36px;text-align:center;font-size:12px;color:#9a9a9a}
</style>
</head>
<body>

<header class="abs hero" role="img" aria-label="Photo of a judge's gavel and scales of justice on a wooden desk with law books"></header>
<div class="abs nav-rule" style="left:152px;top:48px;width:320px"></div>
<div class="abs nav-rule" style="left:152px;top:94px;width:320px"></div>
<div class="abs nav-rule" style="left:746px;top:48px;width:320px"></div>
<div class="abs nav-rule" style="left:746px;top:94px;width:320px"></div>
<nav class="nav">
  <a class="active" style="left:156px">HOME</a>
  <a style="left:228px">ABOUT US</a>
  <a style="left:328px">ATTORNEY PROFILE</a>
  <a style="left:762px">PRACTICE AREAS</a>
  <a style="left:910px">CLIENT</a>
  <a style="left:988px">CONTACT</a>
</nav>
<div class="abs brand">Tidecrest Law</div>
<h1 class="abs hero-title l1">WE ARE A SMALL SOLO</h1>
<h1 class="abs hero-title l2">PRACTICE LAW OFFICE</h1>
<a class="abs btn-red">CONTACT US</a>
<div class="abs dots"><span></span><span></span><span></span><span></span></div>

<section class="welcome">
  <h2 class="abs">WELCOME TO TIDECREST LAW, P.C.</h2>
  <p class="abs" style="top:667px">Find the big firm style legal counsel you can work with in your hometown region at Tidecrest Law P.C., in Chico, CA. Attorney Maren J. Hollis, Esq., offers a boutique law firm opportunity for clients who want to enjoy all the advantages of her broad legal experience and education. She works closely with clients, and has the knowledge of many areas of law to apply to your situation.</p>
  <p class="abs" style="top:773px">This is very helpful when it is necessary to incorporate those different areas of law practice into creating a winning argument for your unique case.</p>
  <a class="abs btn-dark">READ MORE</a>
  <div class="abs cloud" role="img" aria-label="Word cloud of legal terms centred on criminal law"></div>
</section>

<section>
  <div class="abs practice" role="img" aria-label="Photo of attorneys in a meeting under a red tint"></div>
  <h2 class="abs practice-title">PRACTICE AREA</h2>

  <div class="abs area" style="left:136px">
    <svg width="116" height="116" viewBox="0 0 116 116"><circle cx="58" cy="58" r="56" fill="#000" stroke="#fff" stroke-width="3"/><path d="M32 56l12-10 10 4 8-4 12 4 10 8-14 12-4-4-4 4-4-4-4 4-4-4z" fill="#fff"/></svg>
    <h3>Business Law</h3>
    <p>Aitae enim iaculis aliquam Mauris nunc quam venenatis nec euismod sit amet egestas placerat est</p>
  </div>
  <div class="abs area" style="left:370px">
    <svg width="116" height="116" viewBox="0 0 116 116"><circle cx="58" cy="58" r="56" fill="#000" stroke="#fff" stroke-width="3"/><path d="M34 80V44h14v-8h10v44zM60 80V58l12-8 12 8v22z" fill="#fff"/></svg>
    <h3>Real Estate Law</h3>
    <p>Aitae enim iaculis aliquam Mauris nunc quam venenatis nec euismod sit amet egestas placerat est</p>
  </div>
  <div class="abs area" style="left:602px">
    <svg width="116" height="116" viewBox="0 0 116 116"><circle cx="58" cy="58" r="56" fill="#000" stroke="#fff" stroke-width="3"/><path d="M36 80V52h6v28zM48 80V58h6v22zM60 80V64h6v16zM72 80V70h6v10z" fill="#fff"/><path d="M36 44l14 8 12-6 18 14" stroke="#fff" stroke-width="3" fill="none"/></svg>
    <h3>Bankruptcy</h3>
    <p>Aitae enim iaculis aliquam Mauris nunc quam venenatis nec euismod sit amet egestas placerat est</p>
  </div>
  <div class="abs area" style="left:836px">
    <svg width="116" height="116" viewBox="0 0 116 116"><circle cx="58" cy="58" r="56" fill="#000" stroke="#fff" stroke-width="3"/><circle cx="42" cy="42" r="6" fill="#fff"/><circle cx="74" cy="42" r="6" fill="#fff"/><circle cx="58" cy="56" r="5" fill="#fff"/><path d="M34 80V52h16v28zM66 80V52h16v28zM52 80V64h12v16z" fill="#fff"/></svg>
    <h3>Family Law</h3>
    <p>Aitae enim iaculis aliquam Mauris nunc quam venenatis nec euismod sit amet egestas placerat est</p>
  </div>
</section>

<section>
  <div class="abs band-grey"></div>
  <article class="abs card" style="left:140px;top:1334px;width:455px;height:231px">
    <h3>Chico California Attorney</h3>
    <div class="ph" role="img" aria-label="Photo of a justice statue beside law books" style="background:linear-gradient(135deg,#d9c6a8,#8a6d4a 60%,#c9b59a)"></div>
    <p>Find the big firm style legal counsel you can work with in your hometown region at Tidecrest Law P.C., in Chico, CA. Attorney Maren J. Hollis, Esq., offers a boutique law firm opportunity for clients who want to enjoy all the advantages</p>
  </article>
  <article class="abs card" style="left:604px;top:1334px;width:454px;height:231px">
    <h3>Chico CA Law Firm</h3>
    <div class="ph" role="img" aria-label="Photo of a team meeting around a table" style="background:linear-gradient(135deg,#cfd6dd,#8e9aa6 55%,#d9c9b2)"></div>
    <p>When you encounter challenges in your personal or business matters, call Attorney Maren J. Hollis to get the legal counsel you need to make important decisions. Our law firm approach is to work closely with clients to make sure they</p>
  </article>
</section>

<section class="blogs">
  <h2 class="abs">RECENT BLOGS</h2>
  <article class="abs post" style="left:140px">
    <div class="ph" role="img" aria-label="Photo of a handshake over a signed contract" style="background:linear-gradient(135deg,#2a2a2a,#7a7a7a 60%,#d8d8d8)"></div>
    <h3>Pellentesque faucibus</h3>
    <p>Accumsan ultricies elit Maecenas at justo id velit placerat molestie Donec dictum lectus non</p>
    <span class="more">READ MORE</span>
  </article>
  <article class="abs post" style="left:449px">
    <div class="ph" role="img" aria-label="Photo of a columned government building facade" style="background:linear-gradient(135deg,#8e8a82,#c9c4ba 55%,#dfe6ee)"></div>
    <h3>Cum sociis natoque</h3>
    <p>Accumsan ultricies elit Maecenas at justo id velit placerat molestie Donec dictum lectus non</p>
    <span class="more">READ MORE</span>
  </article>
  <article class="abs post" style="left:758px">
    <div class="ph" role="img" aria-label="Photo of a lawyer reviewing documents in a library" style="background:linear-gradient(135deg,#5a3a2a,#8b6a55 55%,#3a2a22)"></div>
    <h3>Etiam eu urna Sed porta Suspendisse</h3>
    <p>Accumsan ultricies elit Maecenas at justo id velit placerat molestie Donec dictum lectus non</p>
    <span class="more">READ MORE</span>
  </article>
</section>

<footer>
  <div class="abs footer" role="img" aria-label="Photo of city office towers at night"></div>
  <div class="abs foot-brand">Tidecrest Law</div>
  <div class="abs fcol" style="left:401px"><h4>Company</h4><ul><li>Home</li><li>About Us</li><li>Our Services</li><li>Case Studies</li></ul></div>
  <div class="abs fcol" style="left:531px"><h4>Resources</h4><ul><li>Team</li><li>Support</li><li>Blogs</li><li>Contact Us</li></ul></div>
  <div class="abs fcol" style="left:679px"><h4>Contact Us</h4><ul>
    <li>Company Name</li>
    <li>48 Harbourne St Eastvale QLD 4090</li>
    <li><svg width="12" height="12" viewBox="0 0 24 24"><path d="M6 2l4 5-2 3a12 12 0 006 6l3-2 5 4-3 4C10 22 2 14 2 5z" fill="#fff"/></svg>(07) 5550 1427</li>
    <li><svg width="12" height="10" viewBox="0 0 24 18"><rect width="24" height="18" rx="2" fill="#fff"/><path d="M1 2l11 8 11-8" stroke="#1a1f2c" stroke-width="2" fill="none"/></svg>hello@tidecrestlaw.com</li>
  </ul></div>
  <div class="abs fcol" style="left:886px"><h4>Follow Us</h4><div class="social" aria-label="Social links"><span></span><span></span><span></span><span></span></div></div>
  <div class="abs bar"><p>© 2016 Company Name&nbsp; All right reserved</p></div>
</footer>

</body>
</html>
```